Building quality affordable homes in Brisbane, Australia for investors and families

We design, build and market our own homes from small single story to large 3 story luxury homes. Our main focus is "duel key" - that is two houses on one lot - a "gribby" (as in where The Gribbs lived) or attached granny flat.
We have a logo design and need a business card to suit. Something simple but eye catching. We want to communicate: "you are making a smart financial choice buying or building with us".
Unfortunately a lot of information has to be on the card including - Name, position, phone, mobile, fax, email, web address and of course the logo.
Logo in multiple formats and high res now available.

Target Market(s)

Families, contractors, real estate agents, other builders, developers, banks and home buyers.

Industry/Entity Type

Financial

Contact Information for Business Card

Name, position, phone, mobile, fax, email, web address

Font styles to use
Serif

Requirements
Must have
• The logo, and the details.
Nice to have
• Show or explain what we do - design, build and market affordable homes.
Should not have
• Nothing too fancy, outrageous - building companies are normally very straight.

```html
<!DOCTYPE html>
<html lang="en">
<head>
<meta charset="utf-8">
<title>Sturdyhome Building Co – Business Card</title>
<link href="https://fonts.googleapis.com/css2?family=Lora:ital,wght@0,400;0,700;1,400&display=swap" rel="stylesheet">
<style>
  :root {
    --brand-blue: #0a72bc;
    --stripe-blue: #7fa8dc;
    --mark-blue: #6c9bd6;
    --paper: #ffffff;
    --backdrop: #d9dbde;
    --ink-white: #ffffff;
  }
  * { margin: 0; padding: 0; box-sizing: border-box; }
  html, body {
    width: 1200px; height: 926px; overflow: hidden;
    background: var(--backdrop);
    font-family: "Lora", Georgia, serif;
  }
  .sheet {
    width: 1200px; height: 926px;
    display: flex; align-items: center; justify-content: center; gap: 40px;
  }
  .card {
    width: 540px; height: 309px; position: relative; overflow: hidden;
    box-shadow: 0 6px 18px rgba(0,0,0,.18);
  }

  /* Brand lockup */
  .brand { display: flex; align-items: center; gap: 12px; }
  .brand-square { width: 46px; height: 46px; flex: none; }
  .brand-name { font-weight: 700; font-size: 30px; line-height: 1.05; }
  .brand-name small { display: block; font-size: 13px; letter-spacing: .3px; margin-top: 4px; font-weight: 700; }

  /* Front side */
  .card-front { background: var(--paper); }
  .card-front .top { height: 138px; display: flex; align-items: center; justify-content: center; }
  .card-front .brand-square { background: var(--mark-blue); }
  .card-front .brand-name { color: var(--brand-blue); }
  .card-front .stripe { height: 8px; background: var(--stripe-blue); }
  .card-front .bottom {
    position: absolute; left: 0; right: 0; top: 146px; bottom: 0;
    background: var(--brand-blue); color: var(--ink-white);
  }
  .person { position: absolute; left: 46px; top: 16px; }
  .person-name { font-size: 22px; font-weight: 400; line-height: 1.2; }
  .person-name b { font-weight: 700; }
  .person-role { font-size: 12.5px; font-style: italic; opacity: .9; margin: 1px 0 6px; }
  .contact-list { list-style: none; font-size: 14px; line-height: 1.4; letter-spacing: .2px; }
  .contact-list em { font-style: italic; }
  .online { position: absolute; left: 288px; bottom: 22px; }

  /* Back side */
  .card-back { background: var(--brand-blue); display: flex; align-items: center; justify-content: center; }
  .card-back .brand-square { background: var(--ink-white); width: 72px; height: 72px; }
  .card-back .brand-name { color: var(--ink-white); font-size: 38px; }
  .card-back .brand-name small { font-size: 16px; }
</style>
</head>
<body>
<main class="sheet">
  <section class="card card-front" aria-label="Business card front">
    <div class="top">
      <div class="brand">
        <span class="brand-square"></span>
        <span class="brand-name">Sturdyhome<small>BUILDING CO PTY LTD</small></span>
      </div>
    </div>
    <div class="stripe"></div>
    <div class="bottom">
      <div class="person">
        <p class="person-name">Mara <b>Quill</b></p>
        <p class="person-role">Sales Manager</p>
        <ul class="contact-list">
          <li><em>phone:</em> 555-201-4410</li>
          <li><em>mobile:</em> 555-318-0927</li>
          <li><em>fax:</em> 555-642-7731</li>
        </ul>
      </div>
      <ul class="contact-list online">
        <li><em>web:</em> sturdyhome.example</li>
        <li><em>email:</em> mara@sturdyhome.example</li>
      </ul>
    </div>
  </section>

  <section class="card card-back" aria-label="Business card back">
    <div class="brand">
      <span class="brand-square"></span>
      <span class="brand-name">Sturdyhome<small>BUILDING CO PTY LTD</small></span>
    </div>
  </section>
</main>
</body>
</html>
```